Flyer für Gästehaus am Bodensee
Zielgruppe
Es soll ein Hausprospekt in Form eines Wickelfalz Fylers (Standard Format, also 10x21 cm Endformat) für ein Gästehaus erstellt werden. Die Texte sollten von Ihnen erstellt werden. Dabei können Sie gerne die Texte der Internetseite (www.gaestehaus-wolkreiter.example) nutzen (entsprechend angepasst). Es werden auch zahlreiche Bilder vom Gästehaus und auch von Attraktionen in der Umgebung zur Verfügung gestellt (Wolkenfach Ablage: https://files.beispielablage.example/ordner?id=7KQ2ZtRmWpLx9NcVbDfGhJ). Diese dürfen aber nur für diese Ausschreibung verwendet werden!
Aufgabenstellung
- Der Flyer soll zeitlos sein (also auch in ein paar Jahren noch funktionieren)
- Der Flyer soll das Interesse am Haus und der Umgebung wecken (einige Ausflugsziele sollten erwähnt werden).
- Die Lage (Uhldingen-Mühlhofen bzw. Unteruhldingen) muss als Vorteil verkauft werden da von hier aus sehr viele Ausflugsziele gut erreicht werden können.
- Die Lage (quasi direkt am See) sollte erkenntlich sein.
- Die fertige Datei wird als PDF (für den Druck und für das Marketing) benötigt.
- Außerdem als Word Datei in der der Kunde selbst etwas ändern kann.
- Auch die Originaldatei von Ihrer Software möchten wir bei Abschluss erhalten.
- Alle Quelldateien (Bilder, Texte, Schriftarten usw.) gehen an uns über (inkl. aller Rechte und Lizenzen).
- Bitten nehmen Sie maximal ein Appartment als Beispiel im Flyer auf (es ist nicht zwangsläufig notwendig, es geht auch ganz ohne). In keinem Fall alle Appartments auflisten.

```html
<!DOCTYPE html>
<html lang="de">
<head>
<meta charset="utf-8">
<title>Gästehaus Wolkreiter – Hausprospekt Innenseite</title>
<link rel="stylesheet" href="https://fonts.googleapis.com/css2?family=PT+Sans:wght@400;700&family=Dancing+Script:wght@500&display=swap">
<style>
  :root {
    --lake-blue: #0d4f86;
    --ink-blue: #154e80;
    --paper: #f4f5f6;
    --backdrop: #e4e5e7;
    --white: #ffffff;
    --fold: rgba(0, 0, 0, 0.06);
  }
  html, body {
    margin: 0;
    width: 1200px;
    height: 795px;
    overflow: hidden;
    background: var(--backdrop);
    font-family: "PT Sans", Arial, sans-serif;
  }
  .spread {
    position: absolute;
    left: 45px;
    top: 48px;
    width: 1110px;
    height: 700px;
    display: flex;
    background: var(--paper);
    box-shadow: 0 6px 24px rgba(0, 0, 0, 0.12);
  }
  .panel {
    position: relative;
    width: 370px;
    height: 700px;
    overflow: hidden;
    box-sizing: border-box;
  }
  .panel + .panel { box-shadow: inset 1px 0 0 var(--fold); }
  .photo { display: block; }
  p { margin: 0; }
  .body-copy {
    font-size: 11.5px;
    line-height: 1.55;
    color: var(--ink-blue);
  }
  strong { font-weight: 700; }

  /* Panel 1: house intro */
  .panel-house {
    display: flex;
    flex-direction: column;
    padding: 100px 30px 0 34px;
  }
  .intro-band {
    position: absolute;
    left: 0; top: 0;
    width: 370px; height: 380px;
    background: var(--lake-blue);
  }
  .panel-house > *:not(.intro-band) { position: relative; }
  .panel-title {
    margin: 0;
    font-family: "Dancing Script", cursive;
    font-weight: 500;
    font-size: 31px;
    line-height: 1.2;
    white-space: nowrap;
    color: var(--white);
  }
  .intro-text {
    margin-top: 12px;
    font-size: 11.5px;
    line-height: 1.55;
    color: var(--white);
  }
  .house-photo {
    margin: 18px 0 0 28px;
    width: 272px; height: 196px;
    border: 4px solid var(--white);
    background: linear-gradient(180deg, #9fc2e0 0%, #c98a62 38%, #b4a590 55%, #5f9640 72%, #3f7a2c 100%);
  }
  .garden-text { margin-top: 26px; }
  .stay-text { margin-top: 12px; }

  /* Panel 2: rooms */
  .panel-rooms { display: flex; flex-direction: column; }
  .living-photo {
    width: 370px; height: 300px; flex: none;
    background: linear-gradient(135deg, #e9e4dc 0%, #c9b7a0 35%, #c9643f 60%, #6e4a3b 80%, #4a362c 100%);
  }
  .rooms-copy { padding: 20px 30px 0 34px; }
  .rules-text { margin-top: 10px; }
  .room-thumbs {
    position: absolute;
    left: 0; bottom: 0;
    width: 370px; height: 140px;
    display: flex;
    gap: 6px;
  }
  .kitchenette-photo {
    flex: 1;
    background: linear-gradient(160deg, #efefef 0%, #c9a073 50%, #8e8f90 100%);
  }
  .double-room-photo {
    flex: 1;
    background: linear-gradient(160deg, #d9c3a0 0%, #c28a56 45%, #f1ece4 65%, #c9463c 100%);
  }

  /* Panel 3: service */
  .panel-service { display: flex; flex-direction: column; }
  .kitchen-photo {
    width: 370px; height: 232px; flex: none;
    background: linear-gradient(135deg, #f2f0ec 0%, #d4cbbf 40%, #c58a4e 60%, #7b7f85 85%, #5a4335 100%);
  }
  .service-band {
    background: var(--lake-blue);
    padding: 20px 30px 22px 30px;
    flex: none;
  }
  .service-text {
    font-size: 11.5px;
    line-height: 1.55;
    color: var(--white);
  }
  .service-text + .service-text { margin-top: 8px; }
  .bedroom-photo {
    flex: 1;
    background: linear-gradient(150deg, #efe6d6 0%, #d9b98a 35%, #c75a33 50%, #f3f1ec 70%, #8c6b4e 100%);
  }
</style>
</head>
<body>
  <main class="spread">
    <section class="panel panel-house">
      <div class="intro-band"></div>
      <h1 class="panel-title">Gästehaus &amp; Appartements</h1>
      <p class="intro-text">Das Gästehaus Wolkreiter liegt in einer der schönsten Urlaubsgegenden der Bodensee-Region, in <strong>Unteruhldingen</strong>, zwischen Meersburg und Überlingen, nur <strong>50 Meter vom See entfernt</strong>, gegenüber der Blumeninsel Mainau. Die schönsten Ausflugsziele am See erreichen Sie innerhalb kurzer Zeit.</p>
      <div class="photo house-photo" role="img" aria-label="Foto: Gästehaus mit rotem Ziegeldach, Balkonen, gepflegtem Garten, Liegewiese und Sonnenschirm"></div>
      <p class="body-copy garden-text">Unsere schöne Liegewiese und der gepflegte Garten sind das richtige Ambiente, wenn Sie sich erholen und ein wenig die Seele baumeln lassen wollen oder nach einem ereignisreichen Urlaubstag sich noch mit anderen Gästen zu einem kleinen Plausch treffen möchten.</p>
      <p class="body-copy stay-text">Ob Sie geschäftlich unterwegs sind oder Ihren Urlaub bei uns verbringen, wir sind stets bemüht, dass Sie sich bei uns wohl fühlen. Bei uns erwartet Sie eine herzliche und familiäre Atmosphäre.</p>
    </section>

    <section class="panel panel-rooms">
      <div class="photo living-photo" role="img" aria-label="Foto: Wohnbereich eines Appartements mit Esstisch, orangefarbener Tischdecke, braunem Ecksofa und Terrassentür zum Garten"></div>
      <div class="rooms-copy">
        <p class="body-copy rooms-text">Unsere Zimmer und Appartements sind komfortabel ausgestattet, damit Sie einen angenehmen und entspannten Urlaub verbringen. Alle Appartements verfügen über eine <strong>Dusche / WC, Küche, Balkon</strong> (teilweise mit Seesicht) oder <strong>Terrasse</strong>. <strong>TV, Telefon, W-LAN, Safe, Bettwäsche</strong> und <strong>Handtücher</strong> gehören ebenso zur Ausstattung und sind inklusiv.</p>
        <p class="body-copy rules-text">Wir haben ausschließlich Nichtraucherzimmer. Gerne können Sie auf dem Balkon oder der Terrasse rauchen. Bitte beachten Sie außerdem, dass in unserem Haus keine Tiere gestattet sind.</p>
      </div>
      <div class="room-thumbs">
        <div class="photo kitchenette-photo" role="img" aria-label="Foto: Flur mit Holztür und Blick in die Küchenzeile"></div>
        <div class="photo double-room-photo" role="img" aria-label="Foto: Doppelzimmer mit Holzbett, weißer Bettwäsche und Tisch mit Blumen"></div>
      </div>
    </section>

    <section class="panel panel-service">
      <div class="photo kitchen-photo" role="img" aria-label="Foto: Moderne Küchenzeile mit Mikrowelle, Kaffeemaschine und grauen Schränken"></div>
      <div class="service-band">
        <p class="service-text">Auf Wunsch verwöhnen wir Sie auch mit einem reichhaltigen Frühstück.</p>
        <p class="service-text">Am Anreisetag stehen die Appartements ab 13.00 Uhr am Abreisetag bis 10.00 Uhr zur Verfügung.</p>
      </div>
      <div class="photo bedroom-photo" role="img" aria-label="Foto: Schlafzimmer mit Doppelbett, orangefarbenem Kopfteil und Leselampen"></div>
    </section>
  </main>
</body>
</html>
```